Vantor Baseball Athletic Training Brochure Design 3 Fold 8x8

I need to create a New 3 page folding brochure for an elite baseball training company that focuses on all aspects of becoming a better baseball player through athletic training. I would like it to be fresh and new. My client likes the Kelmford Harriers colors. It needs to appeal to a young athletic crowd.

HERE IS A WEBSITE FROM A COMPETITOR
https://www.pulvanfit.example/baseball/
I HAVE INCLUEDE A PDF FLYER OF SOMETHING THEIR COMPETITORS HAVE DONE

Target Market(s)

Professional and amateur baseball players

Font styles to use
Sans Serif

Colors
33a6d7
3176b5
000000
b2b2b2

Requirements
Must have
• Images featuring training. I would use BRAXWELD training images as well.
• References:
• "As a former professional baseball player, I know the hard work and dedication it takes to make it and be your best.
• Every athlete that aspires to be the best they can be must out work their opponents on all levels,
• especially when it comes to taking care of your body. Being strong physically is a must with all the
• elite athletes competing. To get an edge, you have to be on a program designed by en experienced trainer
• and leader. With that said, there's nobody I'd recommend higher than Dean Valcourt with Vantor's
• Training.
• -Colby Fenwick
• Founder Bright Arc Hitting
• 12 year Professional Veteran
• "Training at VT in the off-season had my body feeling the best it felt going into Spring Training. My power in hitting, my speed in running, and the quickness of my feet in the infield hadn’t felt this good in a long time."
• -Tobin Marquette, Professional Baseball Player
• "Dean is one of a handful of baseball-specific strength coaches that we choose to refer out to on the west coast when Halvik Sports Performance athletes are in search of quality supervision and an appreciation for the unique needs of this athletic population."
• Co-Owner of HSP, Gordon Ashby-
• "Having played at the professional level, I understand that the demands of the baseball season are tough and recovery is very important, but also realize the off-season is short and this not just a time to recover but get better."
• - Dean Valcourt Owner

```html
<!DOCTYPE html>
<html lang="en">
<head>
<meta charset="utf-8">
<title>Vantor Baseball Athletic Training – Tri-fold Brochure</title>
<link rel="stylesheet" href="https://fonts.googleapis.com/css2?family=Arvo:wght@700&family=Montserrat:wght@400;500&family=Merriweather:wght@300;400&display=swap">
<style>
  :root {
    --stage: #d9dcdf;
    --red-deep: #8e0f18;
    --red: #b8161f;
    --green: #2f8a22;
    --green-deep: #175a26;
    --teal-dark: #0c2424;
    --ink: #0a1719;
    --white: #ffffff;
    --soft-white: #e9ecea;
    --fold: rgba(0, 0, 0, 0.25);
  }
  * { box-sizing: border-box; margin: 0; padding: 0; }
  html, body { width: 1200px; height: 800px; overflow: hidden; }
  body { background: var(--stage); position: relative; }

  .brochure {
    position: absolute;
    left: 30px; top: 200px;
    width: 1140px; height: 400px;
    overflow: hidden;
    background: linear-gradient(100deg, var(--red-deep) 0%, var(--red) 28%, var(--green) 44%, var(--green-deep) 56%, var(--teal-dark) 68%, var(--ink) 100%);
    box-shadow: 0 6px 18px rgba(0,0,0,0.25);
    color: var(--white);
  }

  .photo { position: absolute; top: 0; height: 400px; }
  .photo--kettlebell {
    left: 200px; width: 240px;
    clip-path: polygon(25% 12%, 88% 0, 100% 100%, 0 100%);
    background: linear-gradient(160deg, #3a1a10 0%, #a0481c 45%, #d8893a 70%, #5a2612 100%);
  }
  .photo--batter {
    left: 410px; width: 240px;
    clip-path: polygon(12% 0, 100% 0, 80% 100%, 0 100%);
    background: linear-gradient(170deg, #2c6b2a 0%, #9fb69a 35%, #e6e8e3 55%, #6f8f6b 80%, #1f4a22 100%);
    opacity: 0.9;
  }
  .photo--gym {
    left: 700px; width: 440px;
    clip-path: polygon(10% 0, 100% 0, 100% 100%, 18% 100%);
    background: linear-gradient(135deg, rgba(30,70,66,0.85) 0%, rgba(18,46,44,0.7) 50%, rgba(60,40,20,0.55) 100%);
  }

  .fold { position: absolute; top: 0; width: 1px; height: 400px; background: var(--fold); }
  .fold--one { left: 380px; }
  .fold--two { left: 760px; }

  .heading {
    position: absolute;
    font-family: "Arvo", Georgia, serif;
    font-weight: 700;
    text-transform: uppercase;
    letter-spacing: 1px;
    line-height: 1.05;
    font-size: 20px;
  }
  .heading--about { left: 236px; top: 92px; }
  .heading--results { left: 560px; top: 42px; }
  .heading--what { right: 40px; top: 30px; text-align: right; }

  .body-copy {
    position: absolute;
    font-family: "Montserrat", Arial, sans-serif;
    font-size: 9.5px;
    line-height: 1.4;
  }
  .body-copy--about { left: 26px; top: 122px; width: 205px; }
  .body-copy--what { left: 800px; top: 64px; width: 300px; font-size: 8px; line-height: 1.5; color: var(--soft-white); }

  .quote {
    position: absolute;
    font-family: "Merriweather", Georgia, serif;
    font-weight: 300;
  }
  .quote--motto { left: 40px; top: 306px; width: 130px; font-size: 15px; line-height: 1.2; }
  .quote--testimonial { left: 560px; top: 118px; width: 178px; font-size: 12.5px; line-height: 1.4; }
  .quote-mark { font-weight: 400; margin-right: 3px; }
  .quote cite {
    display: block;
    font-family: "Montserrat", Arial, sans-serif;
    font-style: normal;
    font-size: 9px;
    margin-top: 3px;
  }
  .quote--motto cite { padding-left: 16px; }
  .quote--testimonial cite { text-align: right; font-style: italic; font-size: 10px; }
  .quote cite small { display: block; font-size: 7px; }

  .services { position: absolute; left: 0; top: 0; list-style: none; }
  .service {
    position: absolute;
    display: flex; align-items: center; gap: 8px;
    font-family: "Arvo", Georgia, serif;
    font-weight: 700;
    font-size: 12px;
    text-transform: uppercase;
    letter-spacing: 1px;
  }
  .service--strength { left: 800px; top: 186px; }
  .service--power { left: 840px; top: 236px; }
  .service--explosiveness { left: 876px; top: 286px; }
  .service-photo {
    width: 36px; height: 36px; border-radius: 50%;
    border: 2px solid var(--white);
  }
  .service--strength .service-photo { background: radial-gradient(circle, #6a6a6a, #1a1a1a); }
  .service--power .service-photo { background: radial-gradient(circle, #9bb7cc, #3b4e5c); border-color: #3176b5; }
  .service--explosiveness .service-photo { background: radial-gradient(circle, #b9a88a, #3a2f22); border-color: #d9b52a; }
</style>
</head>
<body>
  <article class="brochure">
    <div class="photo photo--kettlebell" role="img" aria-label="Athlete gripping a kettlebell on a gym floor"></div>
    <div class="photo photo--batter" role="img" aria-label="Baseball player in white uniform finishing a swing"></div>
    <div class="photo photo--gym" role="img" aria-label="Athlete training with battle ropes in a dark gym"></div>

    <span class="fold fold--one"></span>
    <span class="fold fold--two"></span>

    <section class="panel panel--about">
      <h2 class="heading heading--about">About Us</h2>
      <p class="body-copy body-copy--about">At Vantor's training we believe in setting attainable athletic goals for maximum results. As former professional baseball player, I understand the needs of the game and what it takes. Working on both sides, strength and conditioning and baseball development, it helps me understand what the body needs and where the focus should be. It is a marathon and not a sprint but with focus and hard work we will be able to get you optimal athletic and baseball performance.</p>
      <blockquote class="quote quote--motto">
        <span class="quote-mark">&ldquo;</span>Failure to prepare is preparing to fail.
        <cite>- Wade Halloran</cite>
      </blockquote>
    </section>

    <section class="panel panel--results">
      <h2 class="heading heading--results">Result<br>Based<br>Training</h2>
      <blockquote class="quote quote--testimonial">
        <span class="quote-mark">&ldquo;</span>Training at VT in the off-season has my body feeling the best it felt going into Spring Training. My power in hitting, my speed in running, and the quickness of my feet in the infield hadn't felt this good in a long time.
        <cite>- Tobin Marquette<small>Professional Baseball Player</small></cite>
      </blockquote>
    </section>

    <section class="panel panel--services">
      <h2 class="heading heading--what">What We Do</h2>
      <p class="body-copy body-copy--what">Baseball Overview: baseball is a game built on rotational force and quick reactions. Our program builds the strength, speed and mobility each player needs, from the off-season through the long summer schedule. Every plan starts with movement screening, then moves into lifting, sprint work and arm care, so you step onto the field stronger, faster and ready to compete.</p>
      <ul class="services">
        <li class="service service--strength"><span class="service-photo" role="img" aria-label="Strength training photo"></span>Strength</li>
        <li class="service service--power"><span class="service-photo" role="img" aria-label="Power training photo"></span>Power</li>
        <li class="service service--explosiveness"><span class="service-photo" role="img" aria-label="Explosiveness training photo"></span>Explosiveness</li>
      </ul>
    </section>
  </article>
</body>
</html>
```